Lumora Pathway Advisory - Business card design needed

I wish to get business cards designed so that it follows my website design ... http://www.lumora-pathway.org
I need logos for QUVEX 7 and KT Summit Associate for myself which I have uploaded the files.
I wish my qualifications PhD PMP FAICD to be smaller print than my name.
Regards
Leopold
Industry/Entity Type
Business
Contact Information for Business Card
Lumora Pathway Advisory
Dr Leopold Marsh PhD PMP FAICD
Director
PO Box 418 Kelvendale NSW 2093 AUSTRALIA
T:+61 2 9352 6710 M:+61 437 918000 F: +61 2 9368 2000
Email: leopold.marsh@lumora-pathway.org
Website: http://www.lumora-pathway.org

```html
<!DOCTYPE html>
<html lang="en">
<head>
<meta charset="utf-8">
<title>Dr Leopold Marsh – Business Card</title>
<link rel="stylesheet" href="https://fonts.googleapis.com/css2?family=Roboto+Condensed:wght@400;700&display=swap">
<style>
  :root {
    --stage: #2b2119;
    --band-top: #1a8fae;
    --band-bottom: #2cb4cf;
    --wave-navy: #14237a;
    --body-top: #3ff2f4;
    --body-mid: #44ecea;
    --body-bottom: #5cdcb4;
    --name-green: #2f7d16;
    --name-edge: #1c4f0c;
    --ink-red: #7c1c2c;
    --icon-ink: #1e2a2e;
    --cert-fill: #1f9a6a;
    --cert-line: #1d6b4a;
    --partner-fill: #4dc6f0;
    --partner-edge: #c7ecf7;
  }
  * { box-sizing: border-box; margin: 0; padding: 0; }
  html, body {
    width: 922px;
    height: 1200px;
    overflow: hidden;
    background: var(--stage);
  }
  .canvas {
    position: relative;
    width: 922px;
    height: 1200px;
    background: var(--stage);
  }
  .card {
    position: absolute;
    left: 51px;
    top: 335px;
    width: 820px;
    height: 530px;
    border-radius: 12px;
    overflow: hidden;
    background: linear-gradient(180deg, var(--body-top) 0%, var(--body-mid) 55%, var(--body-bottom) 100%);
    font-family: "Roboto Condensed", "Arial Narrow", sans-serif;
    box-shadow: 0 14px 40px rgba(0,0,0,0.5);
  }
  .card-band {
    position: absolute;
    left: 0; top: 0;
    width: 820px;
    height: 130px;
  }
  .cert-badge {
    position: absolute;
    left: 40px;
    top: 140px;
    width: 280px;
    height: 112px;
  }
  .holder {
    position: absolute;
    right: 56px;
    top: 150px;
    text-align: right;
  }
  .holder-name {
    font-weight: 700;
    font-size: 56px;
    line-height: 1;
    color: var(--name-green);
    -webkit-text-stroke: 1px var(--name-edge);
  }
  .holder-quals {
    display: inline-block;
    margin-top: 6px;
    padding-top: 4px;
    padding-left: 150px;
    border-top: 2px solid rgba(255,255,255,0.8);
    font-weight: 700;
    font-size: 18px;
    color: var(--name-edge);
    letter-spacing: 0.5px;
  }
  .contacts {
    position: absolute;
    left: 292px;
    top: 262px;
    list-style: none;
  }
  .contact {
    display: flex;
    align-items: center;
    height: 46px;
    font-size: 31px;
    font-weight: 400;
    color: var(--ink-red);
    white-space: nowrap;
  }
  .contact-icon {
    width: 26px;
    height: 26px;
    margin-right: 18px;
    flex: none;
  }
  .contact-indent { padding-left: 44px; }
  .partner-badge {
    position: absolute;
    right: 32px;
    bottom: 40px;
    width: 186px;
    height: 70px;
    border-radius: 8px;
    background: var(--partner-fill);
    border: 3px solid var(--partner-edge);
  }
</style>
</head>
<body>
<div class="canvas">
  <div class="card">
    <svg class="card-band" viewBox="0 0 820 130" aria-hidden="true">
      <defs>
        <linearGradient id="bandFill" x1="0" y1="0" x2="0" y2="1">
          <stop offset="0" stop-color="var(--band-top)"/>
          <stop offset="1" stop-color="var(--band-bottom)"/>
        </linearGradient>
      </defs>
      <path d="M0,0 H820 V92 C640,60 460,110 300,88 C180,72 80,60 0,118 Z" fill="url(#bandFill)"/>
      <path d="M0,118 C80,60 180,72 300,88 C460,110 640,60 820,92" fill="none" stroke="var(--wave-navy)" stroke-width="7"/>
      <path d="M0,126 C80,70 180,80 300,96 C460,118 640,70 820,100" fill="none" stroke="var(--wave-navy)" stroke-width="1.5" opacity="0.5"/>
    </svg>

    <svg class="cert-badge" viewBox="0 0 280 112" role="img" aria-label="QUVEX 7 certification badge">
      <rect x="1" y="1" width="278" height="110" rx="14" fill="var(--cert-fill)" opacity="0.35"/>
      <rect x="1" y="1" width="278" height="110" rx="14" fill="none" stroke="var(--cert-line)" stroke-width="2"/>
    </svg>

    <div class="holder">
      <div class="holder-name">Dr Leopold Marsh</div>
      <div class="holder-quals">PhD . PMP . FAICD</div>
    </div>

    <ul class="contacts">
      <li class="contact">
        <svg class="contact-icon" viewBox="0 0 24 24" aria-hidden="true">
          <path d="M12 3 L2 12 H5 V21 H10 V15 H14 V21 H19 V12 H22 Z" fill="var(--icon-ink)"/>
        </svg>
        418 Kelvendale NSW 2093 Australia
      </li>
      <li class="contact">
        <svg class="contact-icon" viewBox="0 0 24 24" aria-hidden="true">
          <rect x="2" y="5" width="20" height="14" fill="none" stroke="var(--icon-ink)" stroke-width="2"/>
          <path d="M2 5 L12 13 L22 5 M2 19 L9 11 M22 19 L15 11" fill="none" stroke="var(--icon-ink)" stroke-width="1.6"/>
        </svg>
        leopold.marsh@lumora-pathway.org
      </li>
      <li class="contact">
        <svg class="contact-icon" viewBox="0 0 24 24" aria-hidden="true">
          <circle cx="12" cy="12" r="10" fill="none" stroke="var(--icon-ink)" stroke-width="1.8"/>
          <ellipse cx="12" cy="12" rx="4.5" ry="10" fill="none" stroke="var(--icon-ink)" stroke-width="1.5"/>
          <path d="M2 12 H22 M4 7 H20 M4 17 H20" stroke="var(--icon-ink)" stroke-width="1.4"/>
        </svg>
        www.lumora-pathway.org
      </li>
      <li class="contact">
        <svg class="contact-icon" viewBox="0 0 24 24" aria-hidden="true">
          <circle cx="12" cy="12" r="10.5" fill="none" stroke="var(--icon-ink)" stroke-width="1.6"/>
          <path d="M8 6.5 L10 6 L11 9 L9.6 10.2 C10.4 12 11.8 13.4 13.6 14.3 L14.8 13 L17.8 14 L17.4 16 C13 17 7 11 8 6.5 Z" fill="var(--icon-ink)"/>
        </svg>
        61 437 918000
      </li>
      <li class="contact contact-indent">+612 9368 2000</li>
    </ul>

    <div class="partner-badge" role="img" aria-label="KT Summit Associate partner badge"></div>
  </div>
</div>
</body>
</html>
```